Townhome Multi-Family Property Exterior Sign

Hello. We are looking for a new design for our exterior pylon for for a multi-family housing property in Texas. The design will need to go on a new sign panel to replace the existing (see photo of existing). We are looking to see both modern and contemporary designs. Included the sign should be the name, Loma Brisa Townhomes and the web address www.lomabrisatownhomes.example.

Attached here is a PDF file of the proposed new sign shape. We are open to other shape ideas as well if your design would better suit a more rectangular shape.

Industry/Entity Type

Property

Font styles to use
Serif
Sans Serif

Colors
9bcb3c

Requirements
Must have
• Name of building: Loma Brisa Townhomes
• Website: www.lomabrisatownhomes.example
Nice to have
• Address: 412-590 Halvern Ridge Drive (only if it fits nicely)

```html
<!DOCTYPE html>
<html lang="en">
<head>
<meta charset="utf-8">
<title>Loma Brisa Townhomes – Exterior Sign</title>
<link rel="stylesheet" href="https://fonts.googleapis.com/css2?family=Montserrat:wght@700;800&display=swap">
<style>
  :root {
    --backdrop: #1d1d1f;
    --post: #ffffff;
    --panel-light: #f4f7fa;
    --panel-blue: #d9e9f4;
    --brand-green: #2fae4a;
    --band-green: #1e9e45;
    --band-green-dark: #138a3c;
    --ink-dark: #2c2c31;
    --band-text: #ffffff;
  }
  html, body {
    margin: 0;
    padding: 0;
    width: 1200px;
    height: 1000px;
    overflow: hidden;
    background: var(--backdrop);
  }
  .sign {
    display: block;
    width: 1200px;
    height: 1000px;
  }
  .sign-name {
    font-family: "Montserrat", sans-serif;
    font-weight: 800;
  }
  .sign-name--accent { fill: var(--brand-green); }
  .sign-name--main { fill: var(--ink-dark); }
  .sign-web, .sign-address {
    font-family: "Montserrat", sans-serif;
    font-weight: 700;
    fill: var(--band-text);
  }
  .post { fill: var(--post); }
</style>
</head>
<body>
<svg class="sign" viewBox="0 0 1200 1000" xmlns="http://www.w3.org/2000/svg">
  <defs>
    <linearGradient id="panelFill" x1="0" y1="0" x2="1" y2="1">
      <stop offset="0" stop-color="var(--panel-blue)"/>
      <stop offset="0.45" stop-color="var(--panel-light)"/>
      <stop offset="1" stop-color="var(--panel-blue)"/>
    </linearGradient>
    <linearGradient id="bandFill" x1="0" y1="0" x2="1" y2="0">
      <stop offset="0" stop-color="var(--band-green)"/>
      <stop offset="0.5" stop-color="#2aae4c"/>
      <stop offset="1" stop-color="var(--band-green-dark)"/>
    </linearGradient>
  </defs>

  <!-- posts -->
  <g class="posts">
    <rect class="post" x="26" y="340" width="48" height="436"/>
    <polygon class="post" points="14,340 86,340 86,333 60,320 40,320 14,333"/>
    <rect class="post" x="1125" y="333" width="50" height="443"/>
    <polygon class="post" points="1112,333 1187,333 1187,326 1160,313 1139,313 1112,326"/>
  </g>

  <!-- panel -->
  <path class="panel" fill="url(#panelFill)"
        d="M75 355 C 220 355, 300 222, 600 222 C 900 222, 980 355, 1125 355 L 1125 725 L 75 725 Z"/>

  <!-- green band -->
  <path class="panel-band" fill="url(#bandFill)"
        d="M75 636 C 300 596, 500 582, 620 583 C 800 584, 1000 600, 1125 622 L 1125 725 L 75 725 Z"/>

  <!-- property name -->
  <text class="sign-name sign-name--accent" x="165" y="446" font-size="126" textLength="840" lengthAdjust="spacingAndGlyphs">LOMA BRISA</text>
  <text class="sign-name sign-name--main" x="165" y="561" font-size="126" textLength="840" lengthAdjust="spacingAndGlyphs">TOWNHOMES</text>

  <!-- globe icon -->
  <g class="web-icon" fill="none" stroke="var(--band-text)" stroke-width="2.2">
    <circle cx="216" cy="642" r="14"/>
    <ellipse cx="216" cy="642" rx="6" ry="14"/>
    <line x1="202" y1="642" x2="230" y2="642"/>
    <path d="M204 634 H228 M204 650 H228"/>
  </g>

  <!-- contact -->
  <text class="sign-web" x="246" y="656" font-size="34" textLength="742" lengthAdjust="spacingAndGlyphs">WWW.LOMABRISATOWNHOMES.EXAMPLE</text>
  <text class="sign-address" x="600" y="698" font-size="23" text-anchor="middle">412-590 HALVERN RIDGE DRIVE</text>
</svg>
</body>
</html>
```